Cedar nest sal
Affordable luxury
Professional
Paul dorsey
Doesn't matter, just write anything, will finalize later
Pauldorsey@quillmarsh.net
All I need is a template that suits the logo, I expect a draft template from your side.
It should include, the name, title, company logo, subtitle, website address, physical address, phone number and email. Thank you
Please suggest
Design number 1 will be used
red as second option

```html
<!DOCTYPE html>
<html lang="en">
<head>
<meta charset="utf-8">
<title>Cedar Nest Sal – Business Card</title>
<link href="https://fonts.googleapis.com/css2?family=Open+Sans:ital,wght@0,400;0,600;1,700&display=swap" rel="stylesheet">
<style>
  :root {
    --backdrop: #2e2e2e;
    --card: #ffffff;
    --green: #5a9a1f;
    --green-light: #7cb733;
    --brown: #6b3a16;
    --text: #555555;
    --divider: #d4d4d4;
  }
  html, body {
    margin: 0;
    width: 1200px;
    height: 780px;
    overflow: hidden;
    background: var(--backdrop);
    font-family: "Open Sans", sans-serif;
  }
  .card {
    position: absolute;
    left: 100px;
    top: 105px;
    width: 1000px;
    height: 570px;
    background: var(--card);
    border-radius: 34px;
    overflow: hidden;
  }
  .brand {
    position: absolute;
    left: 70px;
    top: 250px;
    display: flex;
    align-items: center;
    gap: 16px;
  }
  .brand-dot {
    width: 22px;
    height: 22px;
    border-radius: 50%;
    background: var(--green);
  }
  .brand-name {
    margin: 0;
    font-size: 44px;
    font-weight: 600;
    color: var(--brown);
    letter-spacing: 1px;
  }
  .divider {
    position: absolute;
    left: 545px;
    top: 80px;
    width: 1px;
    height: 360px;
    background: var(--divider);
  }
  .details {
    position: absolute;
    left: 580px;
    top: 72px;
    color: var(--text);
  }
  .person-name {
    margin: 0;
    font-size: 30px;
    font-style: italic;
    font-weight: 700;
    color: var(--green);
  }
  .job-title {
    margin: 2px 0 0;
    font-size: 22px;
    color: var(--brown);
  }
  .address {
    margin: 44px 0 0;
    font-size: 19px;
    line-height: 1.35;
  }
  .contacts {
    list-style: none;
    margin: 34px 0 0;
    padding: 0;
    font-size: 19px;
  }
  .contacts li {
    display: flex;
    align-items: center;
    gap: 12px;
    height: 34px;
  }
  .contacts svg { width: 18px; height: 18px; fill: var(--green); flex: none; }
  .bands {
    position: absolute;
    left: 0;
    bottom: 0;
    width: 1000px;
    height: 570px;
  }
</style>
</head>
<body>
  <div class="card">
    <svg class="bands" viewBox="0 0 1000 570" aria-hidden="true">
      <path d="M0 505 L760 492 L735 570 L0 570 Z" fill="var(--green)"/>
      <path d="M0 505 L760 492 L756 505 L0 518 Z" fill="var(--green-light)"/>
      <path d="M775 470 L1000 462 L1000 505 L762 515 Z" fill="var(--brown)"/>
    </svg>

    <div class="brand">
      <span class="brand-dot"></span>
      <p class="brand-name">CEDAR NEST SAL</p>
    </div>

    <div class="divider"></div>

    <div class="details">
      <h1 class="person-name">Paul dorsey</h1>
      <p class="job-title">job title</p>
      <p class="address">Suite 102 Street name,<br>State, Zip 2034,Country</p>
      <ul class="contacts">
        <li>
          <svg viewBox="0 0 24 24"><path d="M6.6 10.8a15 15 0 0 0 6.6 6.6l2.2-2.2c.3-.3.7-.4 1-.2 1.1.4 2.3.6 3.6.6.6 0 1 .4 1 1V20c0 .6-.4 1-1 1A17 17 0 0 1 3 4c0-.6.4-1 1-1h3.5c.6 0 1 .4 1 1 0 1.3.2 2.5.6 3.6.1.3 0 .7-.2 1z"/></svg>
          127 555 0184
        </li>
        <li>
          <svg viewBox="0 0 24 24"><path d="M7 2h10a1 1 0 0 1 1 1v18a1 1 0 0 1-1 1H7a1 1 0 0 1-1-1V3a1 1 0 0 1 1-1zm1 3v12h8V5z"/></svg>
          345 555 0162
        </li>
        <li>
          <svg viewBox="0 0 24 24"><circle cx="12" cy="12" r="10"/><path d="M6 8h12v8H6z M6 8l6 5 6-5" fill="none" stroke="#fff" stroke-width="1.5"/></svg>
          Pauldorsey@quillmarsh.net
        </li>
        <li>
          <svg viewBox="0 0 24 24"><circle cx="12" cy="12" r="10"/><path d="M2 12h20M12 2c3 3 3 17 0 20M12 2c-3 3-3 17 0 20" fill="none" stroke="#fff" stroke-width="1.3"/></svg>
          www.cedarnestsal.com
        </li>
      </ul>
    </div>
  </div>
</body>
</html>
```